Thankyou post card for our customers

we would like to have a design for a post card that we would like to send to our customers once they have hired from us to say thankyou and to offer them a discount on there next hire.

our business is called Wandering Gum Caravan Rentals.
we hire our camper trailers and are based in Australia so alot of our customers go to the outback bush, beach etc with our campers.
the post card dimesions are
Full Bleed Size

213 x 98 mm
2517 x 1158 pixels

Document Trim Size

210 x 95 mm
2481 x 1122 pixels

I want 4 lines for the name and address on the right have side of the post card (like normal post cards have

Industry/Entity Type

Business

Requirements
Must have
• we want it to be double sided so a Design on front and back of post card
I have attached our logo and some other things we have used in previous business material up to you if you want to use what I have uploaded

please note the logo with sunset I have attached I do not want the round logo used just wanted to show you how great the sunset looks we have changed our logo to just be the Wandering Gum Caravan Rentals but wouldnt mind if you used a sunset like this on the whole of the card? but not limited to that.

front of card:
our logo on front page (which is just the Wandering Gum Caravan Rentals attachement WGCR1)
and our details:
P: 0491 326 715
W: www.wanderinggumcaravanrentals.com.au
E:info@wanderinggumcaravanrentals.com.au

and the following to be on the front of the post card:

Dear Fellow Campers,
We hope you have arrived home safely, and are rested and relaxed from your trip away. It was our pleasure to have you hire one of our campers and would like to thankyou for your support, we trust you enjoyed glamping and would like to think you would hire from us again. to show our appreciation we would like to offer you a 20% discount on any minimum 7 day hire over the next 6 months. we look forward to hearing from you again soon.
sincerely,
Graham & Leonie

offer not valid in peak period or in conjuction with any other offer

Full Bleed Size

213 x 98 mm
2517 x 1158 pixels

Document Trim Size

210 x 95 mm
2481 x 1122 pixels

Back of Card:

I want "Thankyou" written at top and then how ever else you design it

```html
<!DOCTYPE html>
<html lang="en">
<head>
<meta charset="utf-8">
<title>Wandering Gum Caravan Rentals – Thank You Postcard (Back)</title>
<link rel="stylesheet" href="https://fonts.googleapis.com/css2?family=Barlow:wght@400;600;700;800&display=swap">
<style>
  :root {
    --card-bg: #f5f5f5;
    --headline: #ffffff;
    --ink-grey: #9a9a9a;
    --rule-grey: #a8a8a8;
  }
  html, body {
    margin: 0;
    padding: 0;
    width: 1200px;
    height: 543px;
    overflow: hidden;
    background: var(--card-bg);
  }
  .postcard-back {
    position: relative;
    width: 1200px;
    height: 543px;
    overflow: hidden;
    background: var(--card-bg);
    font-family: "Barlow", "Helvetica Neue", Arial, sans-serif;
  }
  .headline {
    position: absolute;
    left: 0;
    top: 0;
    width: 1200px;
    height: 170px;
  }
  .headline text {
    font-family: "Barlow", "Helvetica Neue", Arial, sans-serif;
    font-weight: 800;
    font-size: 272px;
    fill: var(--headline);
  }
  .contact {
    position: absolute;
    left: 57px;
    top: 411px;
    color: var(--ink-grey);
    text-transform: uppercase;
    letter-spacing: 0.6px;
  }
  .contact-line {
    margin: 0;
    font-weight: 700;
    font-size: 23px;
    line-height: 27px;
  }
  .offer-terms {
    margin: 2px 0 0;
    font-weight: 400;
    font-size: 18px;
    line-height: 22px;
    letter-spacing: 0.5px;
  }
  .address-lines {
    position: absolute;
    left: 818px;
    top: 280px;
    width: 325px;
  }
  .address-line {
    display: block;
    height: 0;
    border-top: 1.5px solid var(--rule-grey);
    margin-bottom: 67px;
  }
</style>
</head>
<body>
  <main class="postcard-back">
    <svg class="headline" viewBox="0 0 1200 170" aria-label="Thank you">
      <text x="-8" y="160" textLength="1218" lengthAdjust="spacingAndGlyphs">THANK YOU</text>
    </svg>

    <section class="contact">
      <p class="contact-line">T 0491 326 715 - www.wanderinggumcaravanrentals.com.au</p>
      <p class="contact-line">info@wanderinggumcaravanrentals.com.au</p>
      <p class="offer-terms">*Offer not valid in peak period or in conjuction with any other offer</p>
    </section>

    <div class="address-lines" aria-label="Recipient name and address">
      <span class="address-line"></span>
      <span class="address-line"></span>
      <span class="address-line"></span>
      <span class="address-line"></span>
    </div>
  </main>
</body>
</html>
```